Peach Point of Sale Cards for Grocery Retail Markets

We are looking to update our peach point of sale card and price card. The cards will need to be 7" x 11" with a .125 bleed - one sided. See attached for the old versions. We would like this to use photos that look like true Washington State Peaches. Here are the bullet points we would like to use: - New Crop!- Tree Ripened- Excellent FlavorNOTE: The price card just needs to have a space where a retailer can write in the sale price of the item. See attachment with the white box.

Target Market(s)

Retail market shoppers

Requirements
Must have
• Pictures of Peaches Only

```html
<!DOCTYPE html>
<html lang="en">
<head>
<meta charset="utf-8">
<title>Peach Price Card</title>
<link rel="stylesheet" href="https://fonts.googleapis.com/css2?family=Anton&family=Archivo+Black&family=Kaushan+Script&family=Nunito:wght@800&family=Roboto+Condensed:wght@700&family=Yellowtail&display=block">
<style>
  :root {
    --paper: #ffffff;
    --brand-green: #0f6b3a;
    --gold: #d9a521;
    --cream: #fbf1dc;
    --kg-brown: #8a2a1c;
    --script-yellow: #f4e21a;
    --peach-red: #a8231c;
    --peach-dark: #5e120e;
    --peach-orange: #d8641f;
  }
  html, body {
    margin: 0;
    padding: 0;
    overflow: hidden;
    background: var(--paper);
  }
  .card {
    position: relative;
    width: 1200px;
    height: 774px;
    overflow: hidden;
    background: var(--paper);
  }
  .card-art {
    position: absolute;
    inset: 0;
  }
  .brand {
    position: absolute;
    left: 56px;
    top: 52px;
    display: flex;
    align-items: center;
    gap: 14px;
  }
  .brand-dot {
    width: 96px;
    height: 96px;
    border-radius: 50%;
    background: var(--peach-orange);
  }
  .brand-name {
    font-family: "Nunito", sans-serif;
    font-weight: 800;
    font-size: 27px;
    line-height: 28px;
    color: var(--brand-green);
  }
  .headline {
    position: absolute;
    left: 128px;
    top: 359px;
    margin: 0;
    font-family: "Archivo Black", sans-serif;
    font-weight: 400;
    font-size: 54px;
    line-height: 57px;
    letter-spacing: 1px;
    color: var(--cream);
    text-shadow: 3px 4px 0 #5a1a10, 0 0 18px rgba(0,0,0,.35);
    transform: rotate(-16.2deg);
    transform-origin: 0 100%;
    white-space: nowrap;
  }
  .tagline {
    position: absolute;
    left: 330px;
    top: 398px;
    margin: 0;
    font-family: "Yellowtail", "Kaushan Script", cursive;
    font-weight: 400;
    font-size: 92px;
    line-height: 110px;
    color: var(--brand-green);
    -webkit-text-stroke: 3px var(--script-yellow);
    paint-order: stroke fill;
    transform: rotate(-19deg);
    transform-origin: 0 100%;
    white-space: nowrap;
  }
  .benefits {
    position: absolute;
    left: 70px;
    top: 534px;
    margin: 0;
    padding: 0;
    list-style: none;
    font-family: "Roboto Condensed", sans-serif;
    font-weight: 700;
    font-size: 38px;
    line-height: 50px;
    color: var(--cream);
    text-shadow: 2px 3px 0 rgba(60,10,5,.75);
  }
  .fruit-feature {
    position: absolute;
    left: 444px;
    top: 492px;
    width: 380px;
    height: 264px;
  }
  .price-unit {
    position: absolute;
    left: 1080px;
    top: 512px;
    font-family: "Anton", sans-serif;
    font-size: 56px;
    line-height: 1;
    color: var(--kg-brown);
  }
  .price-figure {
    position: absolute;
    left: 920px;
    top: 534px;
    font-family: "Anton", sans-serif;
    font-size: 238px;
    line-height: 1;
    color: var(--brand-green);
  }
  .price-currency {
    position: absolute;
    left: 1042px;
    top: 584px;
    font-family: "Anton", sans-serif;
    font-size: 196px;
    line-height: 1;
    color: var(--brand-green);
  }
</style>
</head>
<body>
<main class="card">
  <svg class="card-art" width="1200" height="774" viewBox="0 0 1200 774" xmlns="http://www.w3.org/2000/svg">
    <defs>
      <radialGradient id="peachField" cx="55%" cy="40%" r="75%">
        <stop offset="0" stop-color="#d8562a"/>
        <stop offset=".45" stop-color="#a8231c"/>
        <stop offset="1" stop-color="#5e120e"/>
      </radialGradient>
    </defs>
    <polygon class="peach-photo" role="img" aria-label="Photograph of a crate full of ripe red and golden Washington peaches"
      points="0,240 872,0 1200,0 1200,436 432,774 0,774" fill="url(#peachField)"/>
    <polygon class="stripe-green" points="445,118 872,0 820,0 478,96" fill="var(--brand-green)"/>
    <polygon class="stripe-gold" points="670,42 820,0 745,0 690,30" fill="var(--gold)"/>
    <polygon class="stripe-gold" points="330,774 352,774 560,706 545,706" fill="var(--gold)"/>
    <polygon class="stripe-green" points="352,774 432,774 590,704 560,704" fill="var(--brand-green)"/>
    <path class="swoosh" d="M530 480 C 700 420, 820 330, 1130 276 C 900 330, 760 420, 530 480 Z" fill="#ffffff"/>
  </svg>

  <div class="brand">
    <div class="brand-dot"></div>
    <div class="brand-name">Evergreen Orchard<br>Council</div>
  </div>

  <h1 class="headline">WASHINGTON STATE PEACHES</h1>
  <p class="tagline">Taste the Difference!</p>

  <ul class="benefits">
    <li>New Crop!</li>
    <li>Tree Ripened</li>
    <li>Excellent Flavor</li>
  </ul>

  <svg class="fruit-feature" viewBox="0 0 380 264" role="img" aria-label="Photograph of whole and halved peaches with green leaves" xmlns="http://www.w3.org/2000/svg">
    <defs>
      <radialGradient id="peachHalf" cx="50%" cy="55%" r="60%">
        <stop offset="0" stop-color="#f2b26a"/>
        <stop offset="1" stop-color="#c9582a"/>
      </radialGradient>
    </defs>
    <ellipse cx="190" cy="176" rx="180" ry="84" fill="url(#peachHalf)"/>
    <ellipse cx="190" cy="70" rx="70" ry="66" fill="#3f8a3a"/>
  </svg>

  <span class="price-unit">KG</span>
  <span class="price-figure">5</span>
  <span class="price-currency">$</span>
</main>
</body>
</html>
```